Medical IT Business with New logo needs a fresh stationary design

First time on pixel Harbor; Thought I would give it a go.
This project is for business cards alone but we have loads of design work that needs to take place in the immediate future.

We provide IT services to the Medical Industry and value ourselves as offering a premium product to the market.

I am after a fresh, clean design using full colour 2 sided cards which includes our current colour palettes from our logo.

Card's must include:
- Logo
- Slogan
- Name
- Adress
- Email
- Phone
- Fax
- Mobile

Target Market(s)

Surgeons, High Profile Medical Personnel

Industry/Entity Type

Business

Fonts, CMYK Colours and Logo files attached.

Requirements
Must have
• Card's must include:
• - Logo
• - Slogan
• - Name
• - Adress
• - Email
• - Phone
• - Fax
• - Mobile
Nice to have
• Needs to incorporate our colour palette (attached CMYK colours)
Should not have
• Black backgrounds. Black text ok.

```html
<!DOCTYPE html>
<html lang="en">
<head>
<meta charset="utf-8">
<title>CareNode Systems – Business Cards</title>
<link rel="stylesheet" href="https://fonts.googleapis.com/css2?family=Open+Sans:wght@300;400;700&display=swap">
<style>
  :root {
    --canvas-bg: #e9edf1;
    --navy: #0f3567;
    --brand-blue: #0a7bb5;
    --paper: #f4f5f7;
    --white: #ffffff;
    --slogan-grey: #8a98aa;
    --card-shadow: 0 10px 30px rgba(15, 53, 103, 0.18);
  }
  * { box-sizing: border-box; margin: 0; padding: 0; }
  html, body {
    width: 1200px;
    height: 900px;
    overflow: hidden;
    background: var(--canvas-bg);
    font-family: "Open Sans", Arial, sans-serif;
  }
  .sheet {
    position: relative;
    width: 1200px;
    height: 900px;
  }
  .card {
    position: absolute;
    left: 285px;
    width: 630px;
    height: 360px;
    overflow: hidden;
    box-shadow: var(--card-shadow);
  }
  /* Front side */
  .card--front {
    top: 65px;
    background: var(--navy);
    display: flex;
    align-items: center;
    justify-content: center;
  }
  .brand {
    display: flex;
    align-items: center;
    gap: 16px;
  }
  .brand__mark {
    border-radius: 50%;
    flex: none;
  }
  .brand__text { display: flex; flex-direction: column; }
  .brand__name {
    font-weight: 700;
    letter-spacing: 1px;
    line-height: 1.05;
    white-space: nowrap;
  }
  .brand__slogan {
    font-weight: 400;
    margin-top: 4px;
    white-space: nowrap;
  }
  .card--front .brand__mark { width: 84px; height: 84px; background: var(--white); }
  .card--front .brand__name { color: var(--white); font-size: 30px; }
  .card--front .brand__slogan { color: var(--white); font-size: 16px; }

  /* Back side */
  .card--back {
    top: 475px;
    background: var(--paper);
  }
  .back__panel {
    position: absolute;
    left: 0; top: 0; bottom: 0;
    width: 250px;
    background: var(--brand-blue);
  }
  .person {
    position: absolute;
    left: 0;
    top: 70px;
    width: 232px;
    text-align: right;
    color: var(--white);
  }
  .person__name { font-size: 26px; font-weight: 700; line-height: 1.1; }
  .person__role { font-size: 15px; font-weight: 400; }

  .card--back .brand {
    position: absolute;
    right: 40px;
    top: 36px;
    gap: 12px;
  }
  .card--back .brand__mark { width: 58px; height: 58px; background: var(--brand-blue); }
  .card--back .brand__name { color: var(--navy); font-size: 20px; }
  .card--back .brand__slogan { color: var(--slogan-grey); font-size: 11px; margin-top: 2px; }

  .contact-tab {
    position: absolute;
    left: 232px;
    top: 150px;
    width: 42px;
    height: 180px;
    background: var(--white);
    border-radius: 8px;
  }
  .contact-list {
    position: absolute;
    left: 237px;
    top: 158px;
    list-style: none;
  }
  .contact-list__item {
    display: flex;
    align-items: center;
    gap: 14px;
    height: 42px;
    color: var(--navy);
    font-size: 14px;
    line-height: 1.25;
  }
  .contact-icon {
    width: 32px;
    height: 32px;
    border-radius: 50%;
    background: var(--navy);
    flex: none;
    display: flex;
    align-items: center;
    justify-content: center;
  }
  .contact-icon svg { width: 16px; height: 16px; fill: var(--white); }
</style>
</head>
<body>
<main class="sheet">

  <section class="card card--front" aria-label="Business card front">
    <div class="brand">
      <span class="brand__mark"></span>
      <div class="brand__text">
        <span class="brand__name">CARENODE SYSTEMS</span>
        <span class="brand__slogan">always beside your clinic</span>
      </div>
    </div>
  </section>

  <section class="card card--back" aria-label="Business card back">
    <div class="back__panel"></div>

    <div class="person">
      <p class="person__name">Alex Marlow</p>
      <p class="person__role">Director</p>
    </div>

    <div class="brand">
      <span class="brand__mark"></span>
      <div class="brand__text">
        <span class="brand__name">CARENODE SYSTEMS</span>
        <span class="brand__slogan">always beside your clinic</span>
      </div>
    </div>

    <div class="contact-tab"></div>
    <ul class="contact-list">
      <li class="contact-list__item">
        <span class="contact-icon">
          <svg viewBox="0 0 24 24"><path d="M6.6 10.8a15.1 15.1 0 0 0 6.6 6.6l2.2-2.2a1 1 0 0 1 1-.25 11.4 11.4 0 0 0 3.6.57 1 1 0 0 1 1 1V20a1 1 0 0 1-1 1A17 17 0 0 1 3 4a1 1 0 0 1 1-1h3.5a1 1 0 0 1 1 1c0 1.25.2 2.45.57 3.57a1 1 0 0 1-.25 1z"/></svg>
        </span>
        <span>0100 555 0147</span>
      </li>
      <li class="contact-list__item">
        <span class="contact-icon">
          <svg viewBox="0 0 24 24"><path d="M7 3h10v5H7zM4 9h16a2 2 0 0 1 2 2v6h-4v4H6v-4H2v-6a2 2 0 0 1 2-2zm4 7v3h8v-3z"/></svg>
        </span>
        <span>0100 555 0148</span>
      </li>
      <li class="contact-list__item">
        <span class="contact-icon">
          <svg viewBox="0 0 24 24"><path d="M3 5h18a1 1 0 0 1 1 1v12a1 1 0 0 1-1 1H3a1 1 0 0 1-1-1V6a1 1 0 0 1 1-1zm9 7.5L20 7H4z"/></svg>
        </span>
        <span>alexmarlow@mailbox.com</span>
      </li>
      <li class="contact-list__item">
        <span class="contact-icon">
          <svg viewBox="0 0 24 24"><path d="M12 2a7 7 0 0 1 7 7c0 5-7 13-7 13S5 14 5 9a7 7 0 0 1 7-7zm0 4.5A2.5 2.5 0 1 0 12 11.5 2.5 2.5 0 0 0 12 6.5z"/></svg>
        </span>
        <span>18 Linden Row<br>Easton, NY 10577</span>
      </li>
    </ul>
  </section>

</main>
</body>
</html>
```